Gift Cards in the Mail Envelope

Mailing out gift cards in the envelope. Need an eye popping envelope. Please look at the enclosed images. The envelope should look like that.

Low design quality

```html
<!DOCTYPE html>
<html lang="en">
<head>
<meta charset="utf-8">
<title>Gift Envelope Template</title>
<link rel="stylesheet" href="https://fonts.googleapis.com/css2?family=Bebas+Neue&family=Open+Sans:wght@300;600&display=swap">
<style>
  :root {
    --paper: #ffffff;
    --envelope-pink: #f8e0e6;
    --fold-line: #f1c8d2;
    --berry-pink: #f4b4c3;
    --navy: #355082;
    --ink: #231f20;
  }
  html, body {
    margin: 0;
    padding: 0;
    overflow: hidden;
    background: var(--paper);
  }
  .sheet {
    position: relative;
    width: 1200px;
    height: 849px;
    overflow: hidden;
    background: var(--paper);
  }
  .instructions {
    position: absolute;
    left: 20px;
    top: 12px;
    margin: 0;
    font-family: "Open Sans", sans-serif;
    color: var(--ink);
    font-size: 15px;
    line-height: 18.5px;
  }
  .instructions__title {
    margin: 0;
    font-size: 15.5px;
    font-weight: 600;
  }
  .instructions__steps {
    margin: 0;
    padding: 0;
    list-style: none;
    font-weight: 300;
    letter-spacing: 0.6px;
  }
  .envelope-net {
    position: absolute;
    left: 0;
    top: 0;
  }
  .greeting {
    position: absolute;
    margin: 0;
    font-family: "Bebas Neue", "Anton", sans-serif;
    font-weight: 400;
    font-size: 90px;
    line-height: 88px;
    white-space: nowrap;
    color: var(--berry-pink);
    text-shadow: -2px 3px 0 var(--navy);
    transform: rotate(90deg);
    transform-origin: left top;
  }
  .greeting--first-line {
    left: 787px;
    top: 250px;
    letter-spacing: 1px;
  }
  .greeting--second-line {
    left: 681px;
    top: 355px;
    letter-spacing: 1px;
  }
</style>
</head>
<body>
<main class="sheet">
  <section class="instructions">
    <h1 class="instructions__title">Simple Envelop Design</h1>
    <ol class="instructions__steps">
      <li>1. Cut the template from the paper</li>
      <li>2. Fold along the lines</li>
      <li>3. Use adhesive or tape to fasten the edges.</li>
      <li>(can de adjusted to preference size)</li>
    </ol>
  </section>

  <svg class="envelope-net" width="1200" height="849" viewBox="0 0 1200 849">
    <defs>
      <linearGradient id="branch-tone" x1="0" y1="0" x2="1" y2="1">
        <stop offset="0" stop-color="#f4b4c3"/>
        <stop offset="1" stop-color="#c7b3c8"/>
      </linearGradient>
    </defs>

    <polygon class="flap flap--top" points="498,128 524,28 914,28 936,128"
             fill="var(--envelope-pink)" stroke="var(--fold-line)" stroke-width="1"/>
    <polygon class="flap flap--bottom" points="498,705 524,805 914,805 936,705"
             fill="var(--envelope-pink)" stroke="var(--fold-line)" stroke-width="1"/>
    <rect class="panel panel--back" x="120" y="128" width="378" height="577"
          fill="var(--envelope-pink)" stroke="var(--fold-line)" stroke-width="1"/>
    <rect class="panel panel--front" x="498" y="128" width="438" height="577"
          fill="var(--envelope-pink)" stroke="var(--fold-line)" stroke-width="1"/>
    <polygon class="flap flap--side" points="936,128 1118,150 1118,681 936,705"
             fill="var(--navy)"/>

    <rect class="berry-branch berry-branch--front-top" x="498" y="128" width="200" height="159"
          fill="url(#branch-tone)" role="img" aria-label="Navy branch with pink berries decoration"/>
    <rect class="berry-branch berry-branch--back-bottom" x="290" y="554" width="208" height="151"
          fill="url(#branch-tone)" role="img" aria-label="Navy branch with pink berries decoration"/>
    <rect class="berry-branch berry-branch--front-bottom" x="729" y="554" width="207" height="151"
          fill="url(#branch-tone)" role="img" aria-label="Navy branch with pink berries decoration"/>
  </svg>

  <p class="greeting greeting--first-line">A GIFT FOR</p>
  <p class="greeting greeting--second-line">YOU</p>
</main>
</body>
</html>
```